Hospital Digital Whiteboard UI/UX Redesign

We are looking to update the look and feel of our Digital Whiteboards.
There are 4 separate layouts: Patient TV, Patient Room Whiteboard, Digital Door Sign, and Unit Care Board.
We want to have a unified, modern look across the portfolio.

```html
<!DOCTYPE html>
<html lang="en">
<head>
<meta charset="utf-8">
<title>VerdantCare Hospital Digital Whiteboard</title>
<link href="https://fonts.googleapis.com/css2?family=Poppins:wght@300;400;500;600;700&display=swap" rel="stylesheet">
<style>
:root{
  --green:#67ab45;
  --ink:#1f2233;
  --text:#3a3d4d;
  --muted:#8a8fa3;
  --line:#e8eaef;
  --stage:#eef0f3;
  --card:#ffffff;
  --blob:#eef3ea;
  --red:#e0382d;
  --orange:#e9831d;
  --wc:#1f7a3a;
  --teal:#14948a;
  --blue:#2a86c9;
  --yellow:#f5c61c;
  --dark:#262a3d;
  --grey:#8f91a6;
  --lightgrey:#e6e6ee;
  --lightgrey2:#f2f2f4;
  --secondary:#97a6bd;
  --extra:#f1f3f6;
}
*{box-sizing:border-box;margin:0;padding:0}
html,body{width:1200px;height:2925px;overflow:hidden}
body{position:relative;background:#fff;font-family:"Poppins",sans-serif;color:var(--text)}
.abs{position:absolute}
.blob{position:absolute;border-radius:50%;background:var(--blob)}
.brand{display:flex;align-items:center;gap:7px;color:var(--green);font-weight:500;white-space:nowrap}
.brand .dot{width:12px;height:12px;border-radius:50%;background:var(--green)}
.tags{top:150px;left:0;width:1200px;display:flex;justify-content:center;gap:20px;color:#c3c6cf;font-size:17px}
.title{top:190px;left:0;width:1200px;text-align:center;font-size:36px;font-weight:500;color:#111;line-height:41px}
.title b{font-weight:700}
.crumb{top:342px;left:0;width:1200px;text-align:center;font-size:15px;color:#333}

.screen{position:absolute;left:60px;width:1080px;height:650px;background:var(--stage);overflow:hidden}
.bar{position:absolute;left:12px;width:1055px;height:48px;background:var(--card);border-radius:4px;display:flex;align-items:center;padding:0 12px}
.avatar{width:27px;height:27px;border-radius:50%;background:var(--green);color:#fff;font-size:14px;display:flex;align-items:center;justify-content:center}
.patient{font-size:19px;color:var(--ink);margin-left:11px}
.bar .brand{position:absolute;left:50%;transform:translateX(-50%);font-size:18px}
.room{margin-left:auto;display:flex;align-items:center;gap:9px;font-size:19px;color:var(--ink)}
.foot{position:absolute;left:12px;width:1055px;height:47px;background:var(--card);border-radius:4px;display:flex;align-items:center;padding:0 16px;font-size:15px;color:var(--ink)}
.foot .time{font-weight:600;margin-left:20px;padding-right:14px;border-right:1px solid var(--line)}
.foot .date{margin-left:13px}
.foot .act{display:flex;align-items:center;gap:8px;margin-left:auto}
.foot .act + .act{margin-left:18px;padding-left:18px;border-left:1px solid var(--line)}

.card{position:absolute;background:var(--card);border-radius:3px;overflow:hidden}
.card-head{height:41px;background:var(--green);color:#fff;font-size:15px;font-weight:500;display:flex;align-items:center;justify-content:center;gap:8px}
.goal-sec{padding:0 14px}
.sec-label{font-size:13px;font-weight:500;color:var(--ink);border-left:3px solid var(--green);padding-left:7px;line-height:15px}
.goal{display:flex;align-items:center;gap:11px;font-size:14px;color:#5a5e6e;height:27.5px;padding-left:10px}
.divider{height:1px;background:var(--line)}
.amb{padding:20px 16px 0 18px;position:relative}
.amb-item{position:relative;padding-left:18px;height:45px}
.amb-item .dot{position:absolute;left:0;top:5px;width:7px;height:7px;border-radius:50%;background:var(--green)}
.amb-item .dot.open{background:#fff;border:1px solid #c8ccd5}
.amb-item .lbl{font-size:13px;color:var(--ink);line-height:16px}
.amb-item .sub{font-size:8.5px;color:var(--muted)}
.amb-line{position:absolute;left:21px;top:30px;height:80px;border-left:1px dashed #c8ccd5}

.member{height:84px;display:flex;align-items:center;padding:0 12px;border-bottom:1px solid var(--line)}
.member:last-child{border-bottom:none}
.photo{width:48px;height:48px;border-radius:50%;flex:none}
.who{margin-left:12px;width:140px}
.role{font-size:9.5px;letter-spacing:1.2px;color:var(--muted);text-transform:uppercase}
.name{font-size:12.5px;font-weight:500;color:var(--ink)}
.phone{display:flex;align-items:center;gap:8px;font-size:12.5px;color:var(--ink);border-left:1px solid var(--line);padding-left:14px;height:30px;margin-left:auto}
.discharge{display:flex;align-items:center;justify-content:center;gap:10px;height:86px;font-size:38px;color:var(--ink)}
.discharge i{width:2px;height:16px;background:#d5d8df}
.dose{height:78px;display:flex;align-items:center;border-bottom:1px solid var(--line)}
.dose:last-child{border-bottom:none}
.pills{width:160px;height:50px;display:flex;justify-content:center;align-items:center;gap:6px}
.tab-round{width:42px;height:42px;border-radius:50%;background:linear-gradient(135deg,#f7f8fa,#e1e3e8)}
.tab-oval{width:44px;height:24px;border-radius:50%;background:linear-gradient(180deg,#f7d093,#eaa550)}
.dose-info{flex:1;border-left:1px solid var(--line);height:40px;display:flex;flex-direction:column;align-items:center;justify-content:center}
.dose-info .role{font-size:9px}
.dose-info .t{font-size:19px;font-weight:500;color:var(--ink)}
.fam{height:40px;display:flex;align-items:center;padding:0 10px 0 13px}
.fam .n{font-size:13px;color:var(--ink);line-height:15px}
.fam .r{font-size:8px;color:var(--muted)}
.fam .phone{font-size:12px;height:26px}

.board{position:absolute;left:12px;top:77px;width:1055px;height:500px;background:var(--card);border-radius:4px}
.board-title{position:absolute;left:18px;top:16px;font-size:16px;font-weight:500;color:var(--ink)}
.show{position:absolute;left:880px;top:17px;font-size:12px;font-weight:500;color:var(--ink)}
.select{position:absolute;left:928px;top:11px;width:116px;height:29px;border:1px solid var(--line);border-radius:3px;font-size:11px;color:var(--ink);display:flex;align-items:center;justify-content:space-between;padding:0 9px}
.row{position:absolute;left:0;width:1055px;display:grid;grid-template-columns:49px 68px 73px 75px 75px 115px 126px 149px 194px 1fr 24px;padding-left:13px;padding-right:14px;align-items:center;font-size:11.5px;color:#555a6b;white-space:nowrap}
.row.head{top:57px;height:26px;font-size:11px;font-weight:500;color:var(--ink)}
.row.data{height:49px;border-top:1px solid var(--line)}
.status{font-size:10px;display:flex;align-items:center;gap:3px}
.status::before{content:"";width:6px;height:6px;border-radius:50%;background:currentColor}
.s-in{color:var(--blue)}.s-vac{color:#a5a9b5}.s-ok{color:#3b9d35}.s-no{color:var(--red)}
.alerts{display:flex;flex-direction:column;gap:5px}
.alert{display:inline-block;padding:0 10px;height:24px;line-height:24px;border-radius:12px;color:#fff;font-size:10px;font-weight:500;width:max-content}
.a-blue{background:var(--blue)}.a-red{background:var(--red)}.a-yel{background:var(--yellow);color:#3a3200}
.flags{display:flex;gap:3px}
.flag{width:32px;height:24px;border-radius:12px;color:#fff;font-size:9.5px;font-weight:600;display:flex;align-items:center;justify-content:center}
.flag.wc{width:37px}
.f-cp{background:var(--red)}.f-ap{background:#e8432b}.f-fr{background:var(--orange)}.f-wc{background:var(--wc)}.f-np{background:var(--teal)}.f-ns{background:#11876f}.f-fry{background:var(--yellow);color:#6b4a00}
.edu{font-size:17px;font-weight:500;color:var(--ink)}

.door-bg{position:absolute;inset:0;background:
  linear-gradient(180deg,rgba(255,255,255,0) 55%,rgba(255,255,255,.6) 100%),
  linear-gradient(90deg,#dfe5ec 0%,#f4f6f9 25%,#eef2f6 45%,#f6f8fa 55%,#c9d6e3 80%,#a9bfd6 100%)}
.door-tab{position:absolute;left:465px;top:24px;width:150px;height:46px;background:#fff;border-radius:0 0 4px 4px;display:flex;align-items:center;justify-content:center}
.door-tab .brand{font-size:17px}
.room-badge{position:absolute;left:430px;top:204px;width:218px;height:50px;background:#fff;color:var(--green);font-size:33px;font-weight:500;display:flex;align-items:center;justify-content:center}
.quote{position:absolute;left:287px;top:277px;width:504px;height:109px;background:#fff;color:var(--ink);font-size:36px;line-height:49px;text-align:center;padding-top:5px}
.ghost{position:absolute;left:0;width:1080px;top:440px;text-align:center;font-size:46px;color:rgba(103,171,69,.08);font-weight:500}

.palette-label{position:absolute;left:62px;font-size:12px;letter-spacing:3px;color:#6b6f7d}
.palette-note{position:absolute;left:62px;font-size:10px;color:#222}
.swatch{position:absolute;width:127px;height:71px}
.sw-name{position:absolute;font-size:15px;color:#6b6f7d}
.sw-hex{position:absolute;font-size:12px;color:#b4b7c1}
</style>
</head>
<body>

<div class="blob" style="left:-60px;top:-60px;width:140px;height:120px"></div>
<div class="blob" style="left:1080px;top:-70px;width:180px;height:160px"></div>
<div class="blob" style="left:950px;top:320px;width:320px;height:320px"></div>
<div class="blob" style="left:-120px;top:380px;width:200px;height:380px"></div>
<div class="blob" style="left:1050px;top:960px;width:220px;height:260px"></div>
<div class="blob" style="left:-140px;top:1050px;width:230px;height:420px"></div>
<div class="blob" style="left:1000px;top:1650px;width:240px;height:260px"></div>

<div class="abs brand" style="left:57px;top:64px;font-size:24px"><span class="dot"></span>Verdant Care</div>

<div class="abs tags"><span>#APP DESIGN</span><span>#UI/UX DESIGN</span><span>#2023</span></div>
<h1 class="abs title"><b>VerdantCare.</b> Hospital Digital<br>Whiteboard</h1>
<div class="abs crumb">Screens / Home</div>

<!-- Patient room whiteboard -->
<section class="screen" style="top:400px">
  <div class="bar" style="top:11px">
    <div class="avatar">A</div><div class="patient">Hollis, Ben</div>
    <div class="brand"><span class="dot"></span>Verdant Care</div>
    <div class="room"><svg width="16" height="17" viewBox="0 0 16 17" fill="none" stroke="#67ab45" stroke-width="1.6"><rect x="2" y="1" width="12" height="15"/><path d="M2 1l6 3v12"/></svg>Room 5131</div>
  </div>

  <div class="card" style="left:12px;top:77px;width:341px;height:289px">
    <div class="card-head"><svg width="16" height="16" viewBox="0 0 16 16" fill="none" stroke="#fff" stroke-width="1.6"><circle cx="8" cy="8" r="6.5"/><circle cx="8" cy="8" r="3"/></svg>Goals</div>
    <div class="goal-sec" style="padding-top:19px">
      <div class="sec-label">Today's Goal</div>
      <div class="goal" style="margin-top:9px"><svg width="16" height="16" viewBox="0 0 16 16" fill="none" stroke="#9aa0ad" stroke-width="1.3"><circle cx="8" cy="8" r="7"/><path d="M4.8 8.2l2.2 2.2 4.2-4.4"/></svg>Walk 25 Feet</div>
    </div>
    <div class="divider" style="margin:11px 0 18px"></div>
    <div class="goal-sec">
      <div class="sec-label">Discharge Goals</div>
      <div class="goal" style="margin-top:6px"><svg width="16" height="16" viewBox="0 0 16 16" fill="none" stroke="#9aa0ad" stroke-width="1.3"><circle cx="8" cy="8" r="7"/><path d="M4.8 8.2l2.2 2.2 4.2-4.4"/></svg>Complete comprehension tests</div>
      <div class="goal"><svg width="16" height="16" viewBox="0 0 16 16" fill="none" stroke="#9aa0ad" stroke-width="1.3"><circle cx="8" cy="8" r="7"/><path d="M4.8 8.2l2.2 2.2 4.2-4.4"/></svg>Review medications</div>
      <div class="goal"><svg width="16" height="16" viewBox="0 0 16 16" fill="none" stroke="#9aa0ad" stroke-width="1.3"><circle cx="8" cy="8" r="7"/><path d="M4.8 8.2l2.2 2.2 4.2-4.4"/></svg>Explain test results</div>
      <div class="goal"><svg width="16" height="16" viewBox="0 0 16 16" fill="none" stroke="#9aa0ad" stroke-width="1.3"><circle cx="8" cy="8" r="7"/><path d="M4.8 8.2l2.2 2.2 4.2-4.4"/></svg>Schedule follow-up appointment</div>
    </div>
  </div>

  <div class="card" style="left:12px;top:379px;width:341px;height:194px">
    <div class="card-head"><svg width="18" height="14" viewBox="0 0 18 14" fill="none" stroke="#fff" stroke-width="1.6"><path d="M1 7h3l2-5 4 10 2-5h5"/></svg>Ambulation Status</div>
    <div class="amb">
      <div class="amb-line"></div>
      <div class="amb-item"><span class="dot"></span><div class="lbl">Moving with support inside room</div><div class="sub">10/21/18</div></div>
      <div class="amb-item"><span class="dot open"></span><div class="lbl">Walking around in hall w/ crutches</div><div class="sub">Goal 10/27/18</div></div>
      <div class="amb-item"><span class="dot open"></span><div class="lbl">Can walk around hall with no help from staff</div><div class="sub">Goal 11/05/18</div></div>
    </div>
  </div>

  <div class="card" style="left:369px;top:77px;width:342px;height:457px">
    <div class="card-head"><svg width="18" height="14" viewBox="0 0 18 14" fill="#fff"><circle cx="9" cy="4" r="3"/><circle cx="3.5" cy="5" r="2.2"/><circle cx="14.5" cy="5" r="2.2"/><path d="M4 13c0-3 2.2-5 5-5s5 2 5 5z"/></svg>Care Team</div>
    <div class="member"><div class="photo" role="img" aria-label="Portrait photo of the nurse manager" style="background:linear-gradient(135deg,#7a93b8,#3b4a6b)"></div><div class="who"><div class="role">Nurse Manager</div><div class="name">Maya Ortiz; R.N.</div></div><div class="phone"><svg width="13" height="13" viewBox="0 0 24 24" fill="#67ab45"><path d="M6.6 10.8a15.1 15.1 0 006.6 6.6l2.2-2.2c.3-.3.7-.4 1-.2 1.1.4 2.3.6 3.6.6.6 0 1 .4 1 1V20c0 .6-.4 1-1 1A17 17 0 013 4c0-.6.4-1 1-1h3.5c.6 0 1 .4 1 1 0 1.3.2 2.5.6 3.6.1.3 0 .7-.2 1z"/></svg>555-010-4114</div></div>
    <div class="member"><div class="photo" role="img" aria-label="Portrait photo of the charge nurse" style="background:linear-gradient(135deg,#e7dcd3,#9d8577)"></div><div class="who"><div class="role">Charge Nurse</div><div class="name">Clara Dunn</div></div><div class="phone"><svg width="13" height="13" viewBox="0 0 24 24" fill="#67ab45"><path d="M6.6 10.8a15.1 15.1 0 006.6 6.6l2.2-2.2c.3-.3.7-.4 1-.2 1.1.4 2.3.6 3.6.6.6 0 1 .4 1 1V20c0 .6-.4 1-1 1A17 17 0 013 4c0-.6.4-1 1-1h3.5c.6 0 1 .4 1 1 0 1.3.2 2.5.6 3.6.1.3 0 .7-.2 1z"/></svg>555-010-4115</div></div>
    <div class="member"><div class="photo" role="img" aria-label="Portrait photo of the duty nurse" style="background:linear-gradient(135deg,#6b4a35,#2f3c70)"></div><div class="who"><div class="role">Duty Nurse</div><div class="name">Renee Pike</div></div><div class="phone"><svg width="13" height="13" viewBox="0 0 24 24" fill="#67ab45"><path d="M6.6 10.8a15.1 15.1 0 006.6 6.6l2.2-2.2c.3-.3.7-.4 1-.2 1.1.4 2.3.6 3.6.6.6 0 1 .4 1 1V20c0 .6-.4 1-1 1A17 17 0 013 4c0-.6.4-1 1-1h3.5c.6 0 1 .4 1 1 0 1.3.2 2.5.6 3.6.1.3 0 .7-.2 1z"/></svg>555-010-4116</div></div>
    <div class="member"><div class="photo" role="img" aria-label="Portrait photo of the patient care tech" style="background:linear-gradient(135deg,#f2f2f2,#3b3f4c)"></div><div class="who"><div class="role">Patient Care Tech</div><div class="name">Omar Reyes</div></div><div class="phone"><svg width="13" height="13" viewBox="0 0 24 24" fill="#67ab45"><path d="M6.6 10.8a15.1 15.1 0 006.6 6.6l2.2-2.2c.3-.3.7-.4 1-.2 1.1.4 2.3.6 3.6.6.6 0 1 .4 1 1V20c0 .6-.4 1-1 1A17 17 0 013 4c0-.6.4-1 1-1h3.5c.6 0 1 .4 1 1 0 1.3.2 2.5.6 3.6.1.3 0 .7-.2 1z"/></svg>555-010-4117</div></div>
    <div class="member"><div class="photo" role="img" aria-label="Portrait photo of the social worker" style="background:linear-gradient(135deg,#f3f3f3,#6a6e7a)"></div><div class="who"><div class="role">Social Worker</div><div class="name">Victor Lane</div></div><div class="phone"><svg width="13" height="13" viewBox="0 0 24 24" fill="#67ab45"><path d="M6.6 10.8a15.1 15.1 0 006.6 6.6l2.2-2.2c.3-.3.7-.4 1-.2 1.1.4 2.3.6 3.6.6.6 0 1 .4 1 1V20c0 .6-.4 1-1 1A17 17 0 013 4c0-.6.4-1 1-1h3.5c.6 0 1 .4 1 1 0 1.3.2 2.5.6 3.6.1.3 0 .7-.2 1z"/></svg>555-010-4118</div></div>
  </div>

  <div class="card" style="left:726px;top:77px;width:342px;height:126px">
    <div class="card-head"><svg width="14" height="14" viewBox="0 0 14 14" fill="none" stroke="#fff" stroke-width="1.5"><rect x="1" y="2.5" width="12" height="10.5" rx="1"/><path d="M1 6h12M4 1v3M10 1v3"/></svg>Anticipated Day of Discharge</div>
    <div class="discharge"><i></i>11/10/2018<i></i></div>
  </div>

  <div class="card" style="left:726px;top:215px;width:342px;height:211px">
    <div class="card-head"><svg width="16" height="16" viewBox="0 0 16 16" fill="none" stroke="#fff" stroke-width="1.5"><rect x="2" y="6" width="12" height="5" rx="2.5" transform="rotate(-35 8 8.5)"/><path d="M6 5l4 6"/></svg>Next Dose</div>
    <div class="dose"><div class="pills" role="img" aria-label="Two round white tablets"><span class="tab-round"></span><span class="tab-round"></span></div><div class="dose-info"><div class="role">Oxycodone 5mg</div><div class="t">11:00AM</div></div></div>
    <div class="dose"><div class="pills" role="img" aria-label="Two oval orange tablets"><span class="tab-oval"></span><span class="tab-oval" style="margin-left:12px"></span></div><div class="dose-info"><div class="role">Odansetron 8mg</div><div class="t">1:30AM</div></div></div>
  </div>

  <div class="card" style="left:726px;top:439px;width:342px;height:134px">
    <div class="card-head"><svg width="16" height="15" viewBox="0 0 16 15" fill="#fff"><circle cx="4" cy="2.3" r="2"/><circle cx="12" cy="2.3" r="2"/><rect x="2" y="5" width="4" height="10" rx="1"/><path d="M10 5h4l1.5 6H13v4h-2v-4H8.5z"/></svg>Family Contact</div>
    <div style="padding-top:6px">
      <div class="fam"><div><div class="n">Paul Hollis</div><div class="r">Dad</div></div><div class="phone"><svg width="13" height="13" viewBox="0 0 24 24" fill="#67ab45"><path d="M6.6 10.8a15.1 15.1 0 006.6 6.6l2.2-2.2c.3-.3.7-.4 1-.2 1.1.4 2.3.6 3.6.6.6 0 1 .4 1 1V20c0 .6-.4 1-1 1A17 17 0 013 4c0-.6.4-1 1-1h3.5c.6 0 1 .4 1 1 0 1.3.2 2.5.6 3.6.1.3 0 .7-.2 1z"/></svg>555-010-4114</div></div>
      <div class="fam"><div><div class="n">Ada Hollis</div><div class="r">Sister</div></div><div class="phone"><svg width="13" height="13" viewBox="0 0 24 24" fill="#67ab45"><path d="M6.6 10.8a15.1 15.1 0 006.6 6.6l2.2-2.2c.3-.3.7-.4 1-.2 1.1.4 2.3.6 3.6.6.6 0 1 .4 1 1V20c0 .6-.4 1-1 1A17 17 0 013 4c0-.6.4-1 1-1h3.5c.6 0 1 .4 1 1 0 1.3.2 2.5.6 3.6.1.3 0 .7-.2 1z"/></svg>555-010-4114</div></div>
    </div>
  </div>

  <div class="foot" style="top:592px">
    <svg width="18" height="14" viewBox="0 0 18 14" fill="none" stroke="#67ab45" stroke-width="1.7"><path d="M5 2L1.5 5.5 5 9M1.5 5.5H12a4 4 0 010 8H9"/></svg>
    <span class="time">10:23AM</span><span class="date">Thursday, October 25th 2018</span>
    <span class="act"><svg width="14" height="14" viewBox="0 0 14 14" fill="#67ab45"><path d="M0 2l4.5-1.5 5 1.5L14 .5v11.5l-4.5 1.5-5-1.5L0 13.5z"/></svg>Floor Map</span>
    <span class="act"><svg width="15" height="15" viewBox="0 0 16 16" fill="#67ab45"><path d="M7 0h2l.4 2.2 1.6.7 1.8-1.3 1.4 1.4-1.3 1.8.7 1.6L16 7v2l-2.2.4-.7 1.6 1.3 1.8-1.4 1.4-1.8-1.3-1.6.7L9 16H7l-.4-2.2-1.6-.7-1.8 1.3-1.4-1.4 1.3-1.8-.7-1.6L0 9V7l2.2-.4.7-1.6-1.3-1.8 1.4-1.4 1.8 1.3 1.6-.7zM8 5a3 3 0 100 6 3 3 0 000-6z"/></svg>Admin</span>
  </div>
</section>

<!-- Unit care board -->
<section class="screen" style="top:1090px">
  <div class="bar" style="top:11px">
    <div class="avatar">A</div><div class="patient">Hollis, Ben</div>
    <div class="brand"><span class="dot"></span>Verdant Care</div>
    <div class="room"><svg width="16" height="17" viewBox="0 0 16 17" fill="none" stroke="#67ab45" stroke-width="1.6"><rect x="2" y="1" width="12" height="15"/><path d="M2 1l6 3v12"/></svg>Room 5131</div>
  </div>

  <div class="board">
    <div class="board-title">Unit 2 West</div>
    <div class="show">Show</div>
    <div class="select">All Patients<svg width="10" height="6" viewBox="0 0 10 6" fill="none" stroke="#1f2233" stroke-width="1.6"><path d="M1 1l4 4 4-4"/></svg></div>

    <div class="row head"><span>RM#</span><span>PATIENT</span><span>PROVIDER</span><span>NURSE</span><span>AIDE</span><span>NEXT ROUND</span><span>RM STATUS</span><span>ALERTS</span><span>FLAGS</span><span>COMPLETED EDU</span><span></span></div>

    <div class="row data" style="top:87px"><span>201</span><span>K.M</span><span>Moreno</span><span>Kessler</span><span>Quinn</span><span>1:30 PM</span><span class="status s-in">Doctor In Room</span><span class="alerts"><span class="alert a-blue">CODE BLUE 00:35</span></span><span class="flags"><span class="flag f-cp">CP</span><span class="flag f-ap">AP</span><span class="flag f-fr">FR</span><span class="flag wc f-wc">WC</span></span><span class="edu">16%</span><svg width="12" height="14" viewBox="0 0 12 14" fill="#7b8091"><path d="M1 2h3a2 2 0 014 0h3v12H1zM3 6h6v1H3zm0 3h6v1H3z"/></svg></div>
    <div class="row data" style="top:136px"><span>202</span><span>M.M</span><span>Harlan</span><span>Brooks</span><span>Tate</span><span>1:15 PM</span><span class="status s-vac">Vacant</span><span></span><span class="flags"><span class="flag f-np">NP</span><span class="flag f-ns">NS</span></span><span class="edu">0%</span><svg width="12" height="14" viewBox="0 0 12 14" fill="#7b8091"><path d="M1 2h3a2 2 0 014 0h3v12H1zM3 6h6v1H3zm0 3h6v1H3z"/></svg></div>
    <div class="row data" style="top:185px"><span>203</span><span>R.H.</span><span>Moreno</span><span>Kessler</span><span>Quinn</span><span>2:35 PM</span><span class="status s-in">Staff in Room</span><span class="alerts"><span class="alert a-red">STAFF EMER 00:35</span></span><span class="flags"><span class="flag f-fry">FR</span></span><span class="edu">40%</span><svg width="12" height="14" viewBox="0 0 12 14" fill="#7b8091"><path d="M1 2h3a2 2 0 014 0h3v12H1zM3 6h6v1H3zm0 3h6v1H3z"/></svg></div>
    <div class="row data" style="top:234px"><span>204</span><span>Z.G.</span><span>Harlan</span><span>Brooks</span><span>Tate</span><span>1:30 PM</span><span class="status s-vac">Vacant</span><span></span><span class="flags"><span class="flag f-fr">FR</span></span><span class="edu">66%</span><svg width="12" height="14" viewBox="0 0 12 14" fill="#7b8091"><path d="M1 2h3a2 2 0 014 0h3v12H1zM3 6h6v1H3zm0 3h6v1H3z"/></svg></div>
    <div class="row data" style="top:283px"><span>205</span><span>D.F.</span><span>Moreno</span><span>Kessler</span><span>Quinn</span><span>1:15 PM</span><span class="status s-ok">Visitors OK</span><span class="alerts"><span class="alert a-blue">WATER 00:35</span></span><span class="flags"><span class="flag f-cp">CP</span><span class="flag f-fr">FR</span><span class="flag wc f-wc">WC</span></span><span class="edu">-</span><svg width="12" height="14" viewBox="0 0 12 14" fill="#7b8091"><path d="M1 2h3a2 2 0 014 0h3v12H1zM3 6h6v1H3zm0 3h6v1H3z"/></svg></div>
    <div class="row data" style="top:332px"><span>206</span><span>A.P.</span><span>Harlan</span><span>Brooks</span><span>Tate</span><span>1:30 PM</span><span class="status s-ok">Visitors OK</span><span class="alerts"><span class="alert a-yel">PULSE OX 00:35</span></span><span class="flags"><span class="flag f-cp">CP</span><span class="flag f-ap">AP</span><span class="flag wc f-wc">WC</span></span><span class="edu">75%</span><svg width="12" height="14" viewBox="0 0 12 14" fill="#7b8091"><path d="M1 2h3a2 2 0 014 0h3v12H1zM3 6h6v1H3zm0 3h6v1H3z"/></svg></div>
    <div class="row data" style="top:381px"><span>207</span><span>S.N.</span><span>Moreno</span><span>Kessler</span><span>Quinn</span><span>2:35 PM</span><span class="status s-ok">Visitors OK</span><span class="alerts"><span class="alert a-red">BED SIDERAIL 00:35</span></span><span class="flags"><span class="flag f-fr">FR</span><span class="flag wc f-wc">WC</span></span><span class="edu">60%</span><svg width="12" height="14" viewBox="0 0 12 14" fill="#7b8091"><path d="M1 2h3a2 2 0 014 0h3v12H1zM3 6h6v1H3zm0 3h6v1H3z"/></svg></div>
    <div class="row data" style="top:430px;height:70px;align-items:start;padding-top:12px"><span>208</span><span>I.Z.</span><span>Harlan</span><span>Brooks</span><span>Tate</span><span>1:30 PM</span><span class="status s-no">NO Visitors</span><span class="alerts" style="margin-top:-6px"><span class="alert a-blue">CODE BLUE 00:35</span><span class="alert a-blue">WATER 00:35</span></span><span class="flags" style="margin-top:-6px"><span class="flag f-cp">CP</span><span class="flag f-fr">FR</span><span class="flag wc f-wc">WC</span></span><span class="edu" style="margin-top:-4px">90%</span><svg width="12" height="14" viewBox="0 0 12 14" fill="#7b8091"><path d="M1 2h3a2 2 0 014 0h3v12H1zM3 6h6v1H3zm0 3h6v1H3z"/></svg></div>
  </div>

  <div class="foot" style="top:591px">
    <svg width="18" height="14" viewBox="0 0 18 14" fill="none" stroke="#67ab45" stroke-width="1.7"><path d="M5 2L1.5 5.5 5 9M1.5 5.5H12a4 4 0 010 8H9"/></svg>
    <span class="time">10:23AM</span><span class="date">Thursday, October 25th 2018</span>
    <span class="act"><svg width="14" height="14" viewBox="0 0 14 14" fill="#67ab45"><path d="M0 2l4.5-1.5 5 1.5L14 .5v11.5l-4.5 1.5-5-1.5L0 13.5z"/></svg>Floor Map</span>
    <span class="act"><svg width="15" height="15" viewBox="0 0 16 16" fill="#67ab45"><path d="M7 0h2l.4 2.2 1.6.7 1.8-1.3 1.4 1.4-1.3 1.8.7 1.6L16 7v2l-2.2.4-.7 1.6 1.3 1.8-1.4 1.4-1.8-1.3-1.6.7L9 16H7l-.4-2.2-1.6-.7-1.8 1.3-1.4-1.4 1.3-1.8-.7-1.6L0 9V7l2.2-.4.7-1.6-1.3-1.8 1.4-1.4 1.8 1.3 1.6-.7zM8 5a3 3 0 100 6 3 3 0 000-6z"/></svg>Admin</span>
  </div>
</section>

<!-- Digital door sign -->
<section class="screen" style="top:1769px">
  <div class="door-bg" role="img" aria-label="Soft blurred photo of a bright hospital corridor"></div>
  <div class="door-tab"><div class="brand"><span class="dot"></span>Verdant Care</div></div>
  <div class="room-badge">ROOM 2016</div>
  <div class="quote">“Believe you can<br>and you’re halfway there.”</div>
  <div class="ghost">Verdant Care</div>
  <div class="foot" style="top:591px">
    <svg width="18" height="14" viewBox="0 0 18 14" fill="none" stroke="#67ab45" stroke-width="1.7"><path d="M5 2L1.5 5.5 5 9M1.5 5.5H12a4 4 0 010 8H9"/></svg>
    <span class="time">10:23AM</span><span class="date">Thursday, October 25th 2018</span>
    <span class="act"><svg width="14" height="14" viewBox="0 0 14 14" fill="#67ab45"><path d="M0 2l4.5-1.5 5 1.5L14 .5v11.5l-4.5 1.5-5-1.5L0 13.5z"/></svg>Floor Map</span>
    <span class="act"><svg width="15" height="15" viewBox="0 0 16 16" fill="#67ab45"><path d="M7 0h2l.4 2.2 1.6.7 1.8-1.3 1.4 1.4-1.3 1.8.7 1.6L16 7v2l-2.2.4-.7 1.6 1.3 1.8-1.4 1.4-1.8-1.3-1.6.7L9 16H7l-.4-2.2-1.6-.7-1.8 1.3-1.4-1.4 1.3-1.8-.7-1.6L0 9V7l2.2-.4.7-1.6-1.3-1.8 1.4-1.4 1.8 1.3 1.6-.7zM8 5a3 3 0 100 6 3 3 0 000-6z"/></svg>Admin</span>
  </div>
</section>

<!-- Colour system -->
<div class="palette-label" style="top:2571px">PRIMARY COLOR</div>
<div class="palette-note" style="top:2601px">Brand or Main Product color for the entire design system.</div>
<div class="swatch" style="left:432px;top:2573px;background:var(--green)"></div>
<div class="swatch" style="left:602px;top:2573px;background:var(--secondary)"></div>
<div class="swatch" style="left:772px;top:2573px;background:var(--extra)"></div>
<div class="sw-name" style="left:442px;top:2652px">Main</div><div class="sw-hex" style="left:442px;top:2677px">#129E8</div>
<div class="sw-name" style="left:611px;top:2652px">Secondary</div><div class="sw-hex" style="left:611px;top:2677px">#19BD9</div>
<div class="sw-name" style="left:782px;top:2652px">Extra</div><div class="sw-hex" style="left:782px;top:2677px">#DCE6E5</div>

<div class="palette-label" style="top:2764px">SYSTEM COLORS</div>
<div class="palette-note" style="top:2794px">Color collections for the entire product ecosystem</div>
<div class="swatch" style="left:432px;top:2766px;background:var(--dark)"></div>
<div class="swatch" style="left:602px;top:2766px;background:var(--grey)"></div>
<div class="swatch" style="left:772px;top:2766px;background:var(--lightgrey)"></div>
<div class="swatch" style="left:942px;top:2766px;background:var(--lightgrey2)"></div>
<div class="sw-name" style="left:442px;top:2845px">Dark</div>
<div class="sw-name" style="left:611px;top:2845px">Grey</div>
<div class="sw-name" style="left:782px;top:2845px">Light Grey</div>
<div class="sw-name" style="left:952px;top:2845px">Light Grey 2</div>

</body>
</html>
```